Lone Mesa Haulworks Garage web site for repairs,Parts, Accessories and Off Road

Need a wed site design for our light duty truck repair shop, also need to be able to sell our products from this page as well. Has our logo as the headliner and brief description of what we do and our history. An example of what we would want it to work like can be seen at www.garvinsfuelworks.example . This is a good example of style and accesses ability to buy parts we have.

Target Market(s)

Light duty Diesel truck owners(Brell,Kastor,Vantorine)

Industry/Entity Type

Shop

Number of Pages Required

3 page

Font styles to use
Other font styles liked:
• The same font as our logo

Requirements
Must have
• A little about the shop and all of our services,availability to purchase our products, also a map of where we are located.
Nice to have
• I like the design of www.Garvinsfuelworks.example. Its easy to use and very descriptive of parts available

```html
<!DOCTYPE html>
<html lang="en">
<head>
<meta charset="utf-8">
<title>Lone Mesa Haulworks Garage</title>
<link href="https://fonts.googleapis.com/css2?family=Open+Sans:wght@400;600;700;800&display=swap" rel="stylesheet">
<style>
:root{
  --bg:#161718;
  --bg-mid:#232527;
  --header:#111213;
  --blue:#1d7fd6;
  --blue-dark:#1667b0;
  --orange:#ef6b16;
  --panel-dark:#1c1d1f;
  --text:#e9e9e9;
  --muted:#9a9da1;
  --line:#34373a;
  --card:#2a2c2f;
}
*{margin:0;padding:0;box-sizing:border-box}
html,body{width:796px;height:1200px;overflow:hidden}
body{font-family:"Open Sans",Arial,sans-serif;color:var(--text);
  background:linear-gradient(180deg,var(--bg-mid) 0,var(--bg) 40%,#1a1b1c 100%);position:relative}
.site-header{position:absolute;top:0;left:0;width:796px;height:58px;background:var(--header);display:flex;align-items:center}
.brand{margin-left:70px;display:flex;align-items:center;gap:7px;height:58px}
.brand-mark{width:12px;height:12px;background:var(--blue)}
.brand-name{font-weight:800;font-size:12px;letter-spacing:.5px;text-transform:uppercase;color:#fff;line-height:1.1;width:120px}
.main-nav{display:flex;gap:30px;margin-left:48px}
.main-nav a{color:#cfd1d3;font-size:9.5px;font-weight:600;text-decoration:none;text-transform:uppercase}
.main-nav a.active{color:#fff;border-bottom:2px solid var(--blue);padding-bottom:4px}
.social{display:flex;gap:7px;margin-left:auto;margin-right:26px}
.social span{width:18px;height:18px;border-radius:50%;background:#3d4043;display:block}
.social span:nth-child(2){background:var(--blue)}
.hero{position:absolute;top:58px;left:0;width:796px;height:340px;
  background:linear-gradient(100deg,#5c6266 0%,#868b8d 30%,#4a4e50 55%,#2a2c2e 80%,#3c3f41 100%)}
.hero-arrow{position:absolute;top:156px;width:20px;height:28px}
.hero-arrow.prev{left:22px}.hero-arrow.next{right:22px}
.hero-dots{position:absolute;right:70px;top:280px;display:flex;gap:5px}
.hero-dots i{width:7px;height:7px;background:#cfcfcf;display:block}
.hero-dots i:first-child{background:var(--orange)}
.feature-row{position:absolute;top:366px;left:66px;width:664px;display:flex;gap:18px}
.feature{flex:1;height:134px;text-align:center;padding-top:16px}
.feature.blue{background:var(--blue)}
.feature.dark{background:var(--panel-dark)}
.feature.orange{background:var(--orange)}
.feature svg{width:34px;height:34px}
.feature h3{font-size:13px;font-weight:800;text-transform:uppercase;margin:8px 0 6px}
.feature p{font-size:8.5px;line-height:1.5;padding:0 18px;color:#f1f1f1}
.welcome{position:absolute;top:544px;left:66px;width:664px}
.welcome h2{font-size:14px;font-weight:800;text-transform:uppercase;margin-top:6px}
.welcome .copy{width:400px;margin-top:10px}
.welcome p{font-size:8.5px;line-height:1.6;color:var(--muted);margin-bottom:9px}
.btn{display:inline-block;background:var(--blue);color:#fff;font-size:8px;font-weight:700;text-transform:uppercase;padding:8px 13px;margin-top:4px}
.video{position:absolute;right:0;top:0;width:240px;height:151px;
  background:linear-gradient(135deg,#5d6063,#8f8c87 45%,#3f4244)}
.video svg{position:absolute;left:100px;top:55px}
.divider{position:absolute;top:742px;left:0;width:796px;height:1px;background:var(--line)}
.products{position:absolute;top:762px;left:66px;width:664px}
.products h2{text-align:center;font-size:14px;font-weight:800;text-transform:uppercase}
.product-grid{display:flex;gap:16px;margin-top:22px}
.product{flex:1;text-align:center}
.product-photo{height:100px;background:var(--card);display:flex;align-items:center;justify-content:center}
.product-photo div{width:70px;height:60px;border-radius:8px}
.product h4{font-size:9.5px;font-weight:400;color:#d6d6d6;margin-top:10px}
.product small{display:block;font-size:7px;color:var(--muted);margin-top:3px}
.stars{font-size:8px;color:#d9a520;letter-spacing:1px}
.buy{display:flex;justify-content:center;gap:6px;margin-top:7px}
.price{border:1px solid #4a4d50;font-size:8.5px;padding:4px 10px;color:#ddd}
.cart{width:22px;height:22px;background:var(--blue);display:flex;align-items:center;justify-content:center}
.site-footer{position:absolute;top:1047px;left:0;width:796px;height:153px;background:#111213;padding:14px 66px 0;display:flex;gap:38px}
.foot-col h5{font-size:8px;font-weight:700;text-transform:uppercase;margin-bottom:6px}
.foot-col li{list-style:none;font-size:7.5px;color:var(--muted);line-height:1.55}
.foot-col p{font-size:7.5px;color:var(--muted);line-height:1.55;width:150px}
.newsletter{margin-left:auto}
.newsletter form{display:flex;margin-top:4px}
.newsletter .field{width:122px;height:20px;background:#fff}
.newsletter .go{width:26px;height:20px;background:var(--blue);font-size:7px;font-weight:700;display:flex;align-items:center;justify-content:center}
.newsletter .social{margin:9px 0 0}
.newsletter .social span{background:#3d4043}
.copyright{font-size:6.5px;color:var(--muted);margin-top:6px}
</style>
</head>
<body>
<header class="site-header">
  <div class="brand"><span class="brand-mark"></span><span class="brand-name">Lone Mesa Haulworks Garage</span></div>
  <nav class="main-nav">
    <a class="active" href="#">Home</a><a href="#">About Us</a><a href="#">Services</a><a href="#">Products</a><a href="#">News</a><a href="#">Contact Us</a>
  </nav>
  <div class="social"><span></span><span></span><span></span></div>
</header>

<section class="hero" role="img" aria-label="Mechanic in safety vest and hard hat kneeling beside the front of a large truck">
  <svg class="hero-arrow prev" viewBox="0 0 20 28"><path d="M15 3 4 14l11 11" fill="none" stroke="#fff" stroke-width="3"/></svg>
  <svg class="hero-arrow next" viewBox="0 0 20 28"><path d="M5 3l11 11L5 25" fill="none" stroke="#fff" stroke-width="3"/></svg>
  <div class="hero-dots"><i></i><i></i><i></i><i></i></div>
</section>

<div class="feature-row">
  <div class="feature blue">
    <svg viewBox="0 0 34 34"><path d="M3 10h17v14H3zM20 15h6l5 5v4H20z" fill="#fff"/><circle cx="9" cy="26" r="3" fill="#fff" stroke="#1d7fd6" stroke-width="1.5"/><circle cx="25" cy="26" r="3" fill="#fff" stroke="#1d7fd6" stroke-width="1.5"/></svg>
    <h3>Shop by Brand</h3>
    <p>Lorem ipsum dolor sit amet, consectetur ad sed do eiusmod tempor incididunt ut labore.</p>
  </div>
  <div class="feature dark">
    <svg viewBox="0 0 34 34"><path d="M5 5h11l14 14-11 11L5 16z" fill="#fff"/><circle cx="11" cy="11" r="2.5" fill="#1c1d1f"/></svg>
    <h3>Shop by Price</h3>
    <p>Lorem ipsum dolor sit amet, consectetur ad sed do eiusmod tempor incididunt ut labore.</p>
  </div>
  <div class="feature orange">
    <svg viewBox="0 0 34 34"><path d="M17 3l4.2 9 9.8 1.1-7.3 6.7 2 9.7L17 24.6 8.3 29.5l2-9.7L3 13.1l9.8-1.1z" fill="#fff"/></svg>
    <h3>Weekly Deals</h3>
    <p>Lorem ipsum dolor sit amet, consectetur ad sed do eiusmod tempor incididunt ut labore.</p>
  </div>
</div>

<section class="welcome">
  <h2>Welcome to our company</h2>
  <div class="copy">
    <p>Lorem ipsum dolor sit amet, consectetur ad sed do eiusmod tempor incididunt ut labore et dolore magna aliqua. Ut enim ad minim veniam, quis nostrud exercitation ullamco laboris nisi ut aliquip ex ea commodo consequat. Duis aute irure dolor in reprehenderit in voluptate velit esse.</p>
    <p>Lorem ipsum dolor sit amet, consectetur ad sed do eiusmod tempor incididunt ut labore et dolore magna aliqua. Ut enim ad minim veniam, quis nostrud exercitation ullamco laboris.</p>
    <span class="btn">Read more</span>
  </div>
  <div class="video" role="img" aria-label="Video still of a mechanic working under a truck">
    <svg width="40" height="40" viewBox="0 0 40 40"><circle cx="20" cy="20" r="19" fill="rgba(0,0,0,.45)"/><path d="M16 12l12 8-12 8z" fill="#fff"/></svg>
  </div>
</section>

<div class="divider"></div>

<section class="products">
  <h2>Our Products</h2>
  <div class="product-grid">
    <div class="product">
      <div class="product-photo" role="img" aria-label="Engine block part"><div style="background:linear-gradient(135deg,#e8a317,#8a5a0c)"></div></div>
      <h4>Product Name</h4><small>Sed ut perspiciatis unde omnis</small><div class="stars">★★★★★</div>
      <div class="buy"><span class="price">£ 60.00</span><span class="cart"><svg width="12" height="12" viewBox="0 0 12 12"><path d="M1 2h2l1.5 6h5.5l1-4.5H4" fill="none" stroke="#fff" stroke-width="1.3"/></svg></span></div>
    </div>
    <div class="product">
      <div class="product-photo" role="img" aria-label="Brake disc part"><div style="background:radial-gradient(circle,#b9b3a8,#6e6a63);border-radius:50%;width:64px;height:64px"></div></div>
      <h4>Product Name</h4><small>Sed ut perspiciatis unde omnis</small><div class="stars">★★★★★</div>
      <div class="buy"><span class="price">£ 60.00</span><span class="cart"><svg width="12" height="12" viewBox="0 0 12 12"><path d="M1 2h2l1.5 6h5.5l1-4.5H4" fill="none" stroke="#fff" stroke-width="1.3"/></svg></span></div>
    </div>
    <div class="product">
      <div class="product-photo" role="img" aria-label="Exhaust manifold part"><div style="background:linear-gradient(135deg,#d8ccb4,#8c8170)"></div></div>
      <h4>Product Name</h4><small>Sed ut perspiciatis unde omnis</small><div class="stars">★★★★★</div>
      <div class="buy"><span class="price">£ 60.00</span><span class="cart"><svg width="12" height="12" viewBox="0 0 12 12"><path d="M1 2h2l1.5 6h5.5l1-4.5H4" fill="none" stroke="#fff" stroke-width="1.3"/></svg></span></div>
    </div>
    <div class="product">
      <div class="product-photo" role="img" aria-label="Clutch plate part"><div style="background:radial-gradient(circle,#c9c9c9,#5d5f62);border-radius:50%;width:64px;height:64px"></div></div>
      <h4>Product Name</h4><small>Sed ut perspiciatis unde omnis</small><div class="stars">★★★★★</div>
      <div class="buy"><span class="price">£ 60.00</span><span class="cart"><svg width="12" height="12" viewBox="0 0 12 12"><path d="M1 2h2l1.5 6h5.5l1-4.5H4" fill="none" stroke="#fff" stroke-width="1.3"/></svg></span></div>
    </div>
  </div>
</section>

<footer class="site-footer">
  <div class="foot-col"><h5>Product</h5><ul><li>Features</li><li>Pricing</li><li>Agencies</li><li>Marketing</li><li>Integrations</li></ul></div>
  <div class="foot-col"><h5>Customers</h5><ul><li>Companies</li><li>Freelancers</li><li>Startups</li><li>Clients</li><li>Support</li></ul></div>
  <div class="foot-col"><h5>Company</h5><ul><li>About</li><li>History</li><li>Team</li><li>Blog</li><li>Careers</li><li>Our Staff</li></ul></div>
  <div class="foot-col"><h5>News</h5><p>Lorem ipsum dolor sit amet, consectetur ad sed do eiusmod.</p><p style="margin-top:8px">Tempor incididunt ut labore et dolore magna aliqua.</p></div>
  <div class="foot-col newsletter"><h5>Join our newsletter</h5>
    <form><span class="field"></span><span class="go">GO</span></form>
    <div class="social"><span></span><span></span><span></span><span></span></div>
    <p class="copyright">Copyright © 2015 All Rights Reserved.</p>
  </div>
</footer>
</body>
</html>
```